" Modo tradicional de funcionamento de drogarias, com diversas seções de produtos, mas evidentemente tendo como principal produto a comercialização de medicamentos. "

```html
<!DOCTYPE html>
<html lang="pt-BR">
<head>
<meta charset="utf-8">
<title>FarmaVida – Papel timbrado</title>
<link rel="stylesheet" href="https://fonts.googleapis.com/css2?family=Nunito:wght@800&family=Open+Sans:wght@400&display=swap">
<style>
  :root {
    --backdrop: #1a8ea8;
    --paper: #ffffff;
    --brand-blue: #2ea3d6;
    --brand-teal: #2bb3a6;
    --mark-faint: #e3f2f8;
    --footer-text: #ffffff;
  }
  html, body {
    margin: 0;
    padding: 0;
    width: 1200px;
    height: 1200px;
    overflow: hidden;
    background: var(--backdrop);
  }
  .letterhead {
    position: absolute;
    left: 210px;
    top: 50px;
    width: 780px;
    height: 1100px;
    background: var(--paper);
    overflow: hidden;
  }
  .letterhead__top-band {
    position: absolute;
    left: 0; top: 0;
    width: 100%;
    height: 16px;
    background: var(--brand-blue);
  }
  .letterhead__brand {
    position: absolute;
    left: 190px;
    top: 46px;
    display: flex;
    align-items: center;
    gap: 10px;
  }
  .letterhead__brand-square {
    width: 22px;
    height: 22px;
    background: var(--brand-blue);
  }
  .letterhead__brand-name {
    font-family: "Nunito", sans-serif;
    font-weight: 800;
    font-size: 34px;
    color: var(--brand-teal);
    letter-spacing: 0.2px;
  }
  .letterhead__watermark {
    position: absolute;
    left: 40px;
    top: 110px;
    width: 700px;
    height: 560px;
    background: radial-gradient(ellipse at 60% 45%, var(--mark-faint) 0%, rgba(227,242,248,0.5) 45%, rgba(255,255,255,0) 75%);
  }
  .letterhead__footer {
    position: absolute;
    left: 0;
    bottom: 0;
    width: 780px;
    height: 120px;
  }
  .letterhead__footer-text {
    position: absolute;
    left: 200px;
    right: 40px;
    bottom: 26px;
    font-family: "Open Sans", sans-serif;
    font-size: 13px;
    line-height: 19px;
    color: var(--footer-text);
    text-align: center;
  }
  .letterhead__footer-text p { margin: 0; }
</style>
</head>
<body>
  <main class="letterhead">
    <div class="letterhead__top-band"></div>

    <div class="letterhead__watermark" role="img" aria-label="Marca d'água suave da drogaria"></div>

    <header class="letterhead__brand">
      <span class="letterhead__brand-square"></span>
      <span class="letterhead__brand-name">FarmaVida</span>
    </header>

    <svg class="letterhead__footer" viewBox="0 0 780 120" aria-hidden="true">
      <path d="M0 120 V40 Q0 22 24 22 H140 Q170 22 180 40 Q190 56 220 56 H730 Q780 56 780 20 V120 Z" fill="#2ea3d6"/>
    </svg>
    <footer class="letterhead__footer-text">
      <p>Rua das Flores, 120 – Centro – São Paulo – SP – CEP 01000-000</p>
      <p>contato@farmavida.com.br – www.farmavida.com.br</p>
      <p>Tel. (11) 4000-1234</p>
    </footer>
  </main>
</body>
</html>
```